Voltrix Power Flyer

Voltrix has developed a device that can properly align incoming electrical current into major energy usage facilities like hotels and hospitals. Designed in the UK, it has shown guaranteed energy savings of 7%. Now being introduced into the USA, our focus is on States that have highest energy costs like Hawaii, CA and NY. I am looking for design help with a 8.5X11 flyer that can be customized for each prospective hotel property client. Content will stay the same and once layout chosen, would like to be able to change the Picture of each prospective hotel site on front of flyer. All the info and basics of layout are established. Simply need some professional help to further design and make it print ready. Logo will need to be adjusted but basic design for that is established also.

```html
<!DOCTYPE html>
<html lang="en">
<head>
<meta charset="utf-8">
<title>Voltrix Power Flyer</title>
<link href="https://fonts.googleapis.com/css2?family=Poppins:ital,wght@0,400;0,500;0,600;0,700;0,800;1,400&display=swap" rel="stylesheet">
<style>
:root{
  --stage:#545655;
  --paper:#ffffff;
  --green:#2a6e55;
  --green-dark:#23614a;
  --lime:#c3d332;
  --navy:#1d3f6e;
  --ink:#2b2b2b;
  --mist:#dfe7e3;
}
*{margin:0;padding:0;box-sizing:border-box}
html,body{width:1200px;height:854px;overflow:hidden;background:var(--stage);font-family:'Poppins',sans-serif;color:var(--ink)}
.page{position:absolute;top:146px;width:435px;height:563px;background:var(--paper);overflow:hidden}
.page--front{left:148px}
.page--back{left:617px}
.abs{position:absolute}

/* front */
.headline{top:24px;left:0;width:100%;text-align:center;font-weight:800;color:var(--green);font-size:15.5px;line-height:18px;letter-spacing:.1px}
.intro{top:77px;left:25px;width:390px;font-size:8.3px;line-height:12.2px}
.hero{top:123px;left:0;width:435px;height:232px}
.savings-figure{top:378px;left:33px;font-weight:800;color:var(--green);font-size:40px;line-height:40px;letter-spacing:-1px}
.savings-figure .pct{font-weight:500;font-size:33px}
.savings-title{top:388px;left:86px;font-weight:800;color:var(--green);font-size:16.5px;line-height:15px}
.savings-sub{top:421px;left:33px;font-size:11.2px;white-space:nowrap}
.savings-sub b{font-weight:700}
.footnote{top:440px;left:32px;font-size:4.6px;font-style:italic}
.checklist{top:368px;left:262px;list-style:none;width:170px}
.checklist li{position:relative;padding-left:15px;font-size:10.3px;line-height:14px;margin-bottom:2px}
.checklist li b{font-weight:700;color:var(--navy)}
.checklist svg{position:absolute;left:0;top:3px}
.footer-band{top:0;left:0}
.brand{font-weight:600;color:var(--green-dark);font-size:19px;letter-spacing:1px;display:flex;align-items:center;gap:7px}
.brand .dot{width:11px;height:11px;border-radius:50%;background:var(--green)}
.page--front .brand{top:521px;left:39px}
.contact{top:516px;left:250px;width:170px;text-align:center;font-size:9.6px;line-height:12.5px}
.contact .name{font-weight:700}
.contact .phone{font-weight:700}

/* back */
.mist{top:0;left:0}
.section-tab{top:25px;left:0;width:217px;height:22px;background:var(--green);border-radius:0 12px 12px 0;color:#fff;font-weight:800;font-size:15.5px;line-height:22px;padding-left:25px;letter-spacing:.3px}
.subhead{top:63px;left:25px;font-weight:700;font-size:11.5px}
.bullets{list-style:none;left:25px;width:200px}
.bullets li{position:relative;padding-left:15px;font-size:10px;line-height:14px;margin-bottom:5px}
.bullets li::before{content:"";position:absolute;left:2px;top:5px;width:5px;height:5px;border-radius:50%;background:var(--ink)}
.bullets--how{top:86px}
.bullets--tech{top:384px;width:202px}
.device-photo{top:25px;left:243px;width:167px;height:243px;border-radius:9px;background:linear-gradient(160deg,#8a8d91,#6c6f73 60%,#55585b)}
.case-title{top:302px;left:25px;font-weight:600;font-size:11.5px}
.case-text{top:324px;left:25px;font-size:10px;line-height:14px}
.case-text b{font-weight:700}
.tech-title{top:366px;left:25px;font-weight:600;font-size:9.6px;letter-spacing:.2px}
.tech-diagram{top:340px;left:236px;width:174px;height:157px;border-radius:7px;background:linear-gradient(135deg,#eef3f4,#d9e7ee 50%,#f2ece2)}
.page--back .brand{top:527px;left:30px;font-size:16px}
</style>
</head>
<body>

<section class="page page--front">
  <h1 class="abs headline">SLASH YOUR MAUI HOTEL’S<br>ENERGY COSTS BY 7%—GUARANTEED</h1>
  <p class="abs intro">In Maui's high-cost, high-use energy environment, Voltrix guarantees a 7% reduction in electricity costs for hotels that install our FlowSet units-and found most properties achieve closer to 10% in real-world conditions.</p>

  <svg class="abs hero" viewBox="0 0 435 232" role="img" aria-label="Photograph of the prospective hotel property: a white resort building with red tile roofs, palm trees and turquoise water">
    <defs>
      <linearGradient id="heroSky" x1="0" y1="0" x2="0" y2="1">
        <stop offset="0" stop-color="#b9dcf3"/>
        <stop offset=".55" stop-color="#e4ddd2"/>
        <stop offset=".8" stop-color="#4f7a3d"/>
        <stop offset="1" stop-color="#4cb7d4"/>
      </linearGradient>
    </defs>
    <path d="M0 0H435V198Q300 245 150 225Q60 215 0 192Z" fill="url(#heroSky)"/>
  </svg>

  <div class="abs savings-figure">7<span class="pct">%</span></div>
  <div class="abs savings-title">ENERGY SAVINGS<br>GUARANTEED</div>
  <p class="abs savings-sub">Most properties see closer to <b>10%</b>**</p>
  <p class="abs footnote">*Actual savings depend on your facility's energy usage patterns.</p>

  <ul class="abs checklist">
    <li><svg width="8" height="7" viewBox="0 0 8 7"><path d="M1 3.5L3 5.5L7 1" fill="none" stroke="#1d3f6e" stroke-width="1"/></svg><b>7% lower electricity costs</b>, guaranteed</li>
    <li><svg width="8" height="7" viewBox="0 0 8 7"><path d="M1 3.5L3 5.5L7 1" fill="none" stroke="#1d3f6e" stroke-width="1"/></svg><b>No upfront</b> capital investment required</li>
    <li><svg width="8" height="7" viewBox="0 0 8 7"><path d="M1 3.5L3 5.5L7 1" fill="none" stroke="#1d3f6e" stroke-width="1"/></svg><b>Zero maintenance</b>, automated solution that starts saving on day one.</li>
  </ul>

  <svg class="abs footer-band" width="435" height="563" viewBox="0 0 435 563">
    <path d="M0 465Q220 500 435 465V563H0Z" fill="var(--green)"/>
    <path d="M0 482Q220 502 435 480V563H0Z" fill="var(--lime)"/>
  </svg>

  <div class="abs brand"><span class="dot"></span>KAIMANA ENERGY</div>
  <div class="abs contact">
    <div class="name">DANIEL KEALOHA</div>
    <div>dk.services808@example.com</div>
    <div class="phone">(808) 555-0147</div>
  </div>
</section>

<section class="page page--back">
  <svg class="abs mist" width="435" height="563" viewBox="0 0 435 563">
    <path d="M0 264Q200 320 435 262V563H0Z" fill="var(--mist)"/>
  </svg>

  <div class="abs section-tab">HOW IT WORKS</div>
  <h2 class="abs subhead">7% Energy Reduction Guaranteed</h2>
  <ul class="abs bullets bullets--how">
    <li>Voltrix installs units at high-use electrical points in your hotel.</li>
    <li>We guarantee a minimum 7% reduction in electricity cost, with most properties achieving closer to 10%.</li>
    <li>No upfront costs —savings start immediately, and Voltrix simply shares a fraction of those savings. No risk to you.</li>
    <li>No maintenance or disruption. Just consistent lower bills.</li>
  </ul>

  <div class="abs device-photo" role="img" aria-label="Photograph of an installed energy saving unit mounted beside an electrical panel"></div>

  <h2 class="abs case-title">Real Results Case Study</h2>
  <p class="abs case-text">4-star UK hotel lowered their<br>electricity bill by <b>10.4%</b></p>

  <h3 class="abs tech-title">FLOWSET TECHNOLOGY</h3>
  <ul class="abs bullets bullets--tech">
    <li>FlowSet devices leverage advanced nanotechnology and spintronics to realign magnetic wave energy within your hotel's electrical system.</li>
    <li>By aligning electron spin, FlowSet units optimize the flow of electricity, reducing waste and improving overall energy efficiency.</li>
  </ul>

  <div class="abs tech-diagram" role="img" aria-label="Illustration of electron particles flowing through aligning filter blocks"></div>

  <div class="abs brand"><span class="dot"></span>KAIMANA ENERGY</div>
</section>

</body>
</html>
```